A property investment company, looking to provide lovely sustainable homes for familys and individua

For a small investment business i am starting which will buy and refurbish unloved houses and apartments to rent out or resell. the company name is my family surname (HARGREAVE). <br/>i would like the design to be simple with maybe some emphasis on an ethical and sustainable/environmentally friendly approach with a branding of maybe trees blended with some houses and or apartments.<br/>The colours i like for this design would be mainly green on either a white or black background.
Target Market(s)
This business card is to be used for professional people such as estate agents
mortgage brokers, solicitors and trades people.
Industry/Entity Type
Real Estate
Contact Information for Business Card
owner/director-Martin hargreave
e-mail-martin@hwlettings.co.uk
website-hargreavehomeholdings.co.uk
mobile-07934560218
landline-02086543107

```html
<!DOCTYPE html>
<html lang="en">
<head>
<meta charset="utf-8">
<title>Hargreave – Business Card</title>
<link href="https://fonts.googleapis.com/css2?family=Source+Sans+3:wght@400;600&display=swap" rel="stylesheet">
<style>
  :root {
    --paper: #ffffff;
    --leaf-green: #8dc63f;
    --forest-green: #0f9a48;
    --teal: #35b493;
    --icon-green: #3aaa35;
    --ink: #444444;
    --ink-soft: #555555;
  }
  * { margin: 0; padding: 0; box-sizing: border-box; }
  html, body {
    width: 1200px;
    height: 686px;
    overflow: hidden;
    background: var(--paper);
  }
  .card {
    position: relative;
    width: 1200px;
    height: 686px;
    background: var(--paper);
    font-family: "Source Sans 3", "Myriad Pro", sans-serif;
    overflow: hidden;
  }
  .brand {
    position: absolute;
    left: 105px;
    top: 183px;
    width: 325px;
    height: 320px;
    display: flex;
    flex-direction: column;
    align-items: center;
    justify-content: center;
    gap: 28px;
  }
  .brand-square {
    width: 72px;
    height: 72px;
    background: var(--teal);
  }
  .brand-name {
    font-size: 46px;
    font-weight: 600;
    letter-spacing: 4px;
    color: var(--leaf-green);
  }
  .divider {
    position: absolute;
    left: 495px;
    top: 120px;
    width: 11px;
    height: 446px;
    background: var(--teal);
  }
  .person {
    position: absolute;
    left: 821px;
    top: 102px;
  }
  .person-name {
    font-size: 44px;
    font-weight: 400;
    color: var(--leaf-green);
    line-height: 1;
  }
  .person-role {
    margin-top: 10px;
    font-size: 30px;
    color: var(--ink-soft);
    line-height: 1;
  }
  .contacts {
    position: absolute;
    left: 628px;
    top: 412px;
    list-style: none;
  }
  .contact {
    display: flex;
    align-items: center;
    height: 58px;
    font-size: 33px;
    color: var(--ink);
  }
  .contact-icon {
    width: 38px;
    height: 34px;
    margin-right: 20px;
    flex: none;
  }
  .contact-icon svg { width: 100%; height: 100%; display: block; fill: var(--icon-green); }
  .web-band {
    position: absolute;
    left: 0;
    bottom: 0;
    width: 1200px;
    height: 48px;
    background: linear-gradient(90deg, var(--forest-green), var(--leaf-green));
    display: flex;
    align-items: center;
    justify-content: center;
  }
  .web-address {
    color: #ffffff;
    font-size: 30px;
    letter-spacing: 5px;
    margin-left: -5px;
  }
</style>
</head>
<body>
  <main class="card">
    <div class="brand">
      <div class="brand-square"></div>
      <div class="brand-name">HARGREAVE</div>
    </div>

    <div class="divider"></div>

    <header class="person">
      <h1 class="person-name">Martin hargreave</h1>
      <p class="person-role">Owner</p>
    </header>

    <ul class="contacts">
      <li class="contact">
        <span class="contact-icon">
          <svg viewBox="0 0 24 24"><path d="M6.6 10.8c1.4 2.8 3.8 5.1 6.6 6.6l2.2-2.2c.3-.3.7-.4 1-.2 1.1.4 2.3.6 3.6.6.6 0 1 .4 1 1V20c0 .6-.4 1-1 1C10.6 21 3 13.4 3 4c0-.6.4-1 1-1h3.5c.6 0 1 .4 1 1 0 1.3.2 2.5.6 3.6.1.3 0 .7-.2 1l-2.3 2.2z"/></svg>
        </span>
        07934560218
      </li>
      <li class="contact">
        <span class="contact-icon">
          <svg viewBox="0 0 24 24"><path d="M7.5 1h9A2.5 2.5 0 0 1 19 3.5v17a2.5 2.5 0 0 1-2.5 2.5h-9A2.5 2.5 0 0 1 5 20.5v-17A2.5 2.5 0 0 1 7.5 1zM7.5 4v14h9V4h-9zM12 19.2a1.1 1.1 0 1 0 0 2.2 1.1 1.1 0 0 0 0-2.2z"/></svg>
        </span>
        02086543107
      </li>
      <li class="contact">
        <span class="contact-icon">
          <svg viewBox="0 0 24 18"><path d="M0 0h24v18H0zM2 2.2v.4l10 7.2 10-7.2v-.4zM2 5v11h20V5l-10 7.2z"/></svg>
        </span>
        martin@hwlettings.co.uk
      </li>
    </ul>

    <footer class="web-band">
      <span class="web-address">www.hargreavehomeholdings.co.uk</span>
    </footer>
  </main>
</body>
</html>
```